Talvero Networks LLC
Consultant, Health Care Operations
Talvero Networks LLC -
Creative Brief
Use specific fonts
I like Calibri, Tahoma, Lucida (rounded but professional) but am open to other similar fonts
Simple
Dwight Pennock
President, CEO
PO BOX 418263 Harbor Glen, FL 30999
dwight@talverohub.com
talverohub.com

```html
<!DOCTYPE html>
<html lang="en">
<head>
<meta charset="utf-8">
<title>Talvero Networks LLC – Stationery Set</title>
<link href="https://fonts.googleapis.com/css2?family=Lato:wght@400;700;900&display=swap" rel="stylesheet">
<style>
  :root {
    --sky: #1aa6e6;
    --navy: #1c2740;
    --ink: #3a3f47;
    --muted: #7a8088;
    --paper: #ffffff;
    --charcoal: #262626;
    --backdrop: #6a3a20;
  }
  * { box-sizing: border-box; margin: 0; padding: 0; }
  html, body { width: 1200px; height: 497px; overflow: hidden; }
  body {
    background: var(--backdrop);
    font-family: "Lato", Tahoma, sans-serif;
    color: var(--ink);
    position: relative;
  }
  .piece { position: absolute; background: var(--paper); box-shadow: 0 2px 6px rgba(0,0,0,.35); overflow: hidden; }

  .wordmark { display: flex; align-items: center; gap: 4px; font-weight: 900; letter-spacing: .5px; color: var(--navy); line-height: 1; white-space: nowrap; }
  .wordmark .dot { border-radius: 50%; background: var(--sky); flex: none; }
  .wordmark.light { color: var(--paper); }
  .wordmark.light .dot { background: var(--paper); }

  /* Business cards */
  .card { width: 200px; height: 115px; border-radius: 7px; }
  .card-front { top: 65px; border-left: 8px solid var(--sky); }
  .card-front.first { left: 20px; }
  .card-front.second { left: 230px; }
  .card-front .wordmark { position: absolute; left: 10px; top: 56px; font-size: 14px; }
  .card-front .wordmark .dot { width: 8px; height: 8px; }
  .card-front .holder { position: absolute; left: 92px; top: 10px; }
  .holder .name { font-size: 7.5px; color: var(--sky); font-weight: 700; }
  .holder .role { font-size: 5.5px; color: var(--muted); margin-top: 1px; }
  .card-front .details { position: absolute; left: 96px; top: 34px; font-size: 5px; line-height: 1.4; color: var(--ink); }
  .details .company { font-weight: 700; }

  .card-back { top: 192px; display: flex; align-items: center; justify-content: center; }
  .card-back.blue { left: 20px; background: var(--sky); }
  .card-back.dark { left: 230px; background: var(--charcoal); }
  .card-back .wordmark { font-size: 22px; }
  .card-back .wordmark .dot { width: 11px; height: 11px; }

  /* Letterhead */
  .letterhead { left: 434px; top: 29px; width: 214px; height: 369px; border-left: 4px solid var(--sky); }
  .letterhead .wordmark { position: absolute; left: 12px; top: 40px; font-size: 14px; }
  .letterhead .wordmark .dot { width: 8px; height: 8px; }
  .letterhead .sender { position: absolute; left: 100px; top: 20px; font-size: 4.5px; line-height: 1.45; color: var(--muted); }
  .letterhead .contact { position: absolute; left: 100px; top: 40px; font-size: 4.5px; line-height: 1.45; color: var(--ink); }
  .contact .label { color: var(--sky); font-weight: 700; }

  /* Envelopes */
  .envelope svg.flap { position: absolute; left: 0; top: 0; }
  .envelope-black { left: 732px; top: 29px; width: 456px; height: 120px; }
  .envelope-black .wordmark { position: absolute; left: 50%; top: 34px; transform: translateX(-50%); font-size: 16px; }
  .envelope-black .wordmark .dot { width: 9px; height: 9px; }

  .envelope-plain { left: 786px; top: 125px; width: 402px; height: 124px; }
  .envelope-plain .wordmark { position: absolute; left: 50%; top: 30px; transform: translateX(-50%); font-size: 14px; }
  .envelope-plain .wordmark .dot { width: 8px; height: 8px; }

  .envelope-blue { left: 662px; top: 185px; width: 386px; height: 195px; }
  .envelope-blue .wordmark { position: absolute; left: 50%; top: 44px; transform: translateX(-50%); font-size: 16px; }
  .envelope-blue .wordmark .dot { width: 9px; height: 9px; background: var(--navy); }
  .envelope-blue .return { position: absolute; left: 17px; top: 112px; font-size: 5px; line-height: 1.45; color: var(--ink); }
</style>
</head>
<body>

  <section class="piece card card-front first">
    <div class="holder"><div class="name">Dwight Pennock</div><div class="role">President, CEO</div></div>
    <div class="wordmark"><span class="dot"></span>TALVERO</div>
    <div class="details">
      <div class="company">Talvero Networks LLC</div>
      <div>PO BOX 418263</div>
      <div>Harbor Glen, FL 30999</div>
      <div>Phone: 954-555-0142</div>
      <div>Skype: pennockd</div>
      <div>dwight@talverohub.com</div>
      <div>talverohub.com</div>
    </div>
  </section>

  <section class="piece card card-front second">
    <div class="holder"><div class="name">Dwight Pennock</div><div class="role">President, CEO</div></div>
    <div class="wordmark"><span class="dot"></span>TALVERO</div>
    <div class="details">
      <div class="company">Talvero Networks LLC</div>
      <div>PO BOX 418263</div>
      <div>Harbor Glen, FL 30999</div>
      <div>Phone: 954-555-0142</div>
      <div>Skype: pennockd</div>
      <div>dwight@talverohub.com</div>
      <div>talverohub.com</div>
    </div>
  </section>

  <section class="piece card card-back blue">
    <div class="wordmark light"><span class="dot"></span>TALVERO</div>
  </section>
  <section class="piece card card-back dark">
    <div class="wordmark light"><span class="dot"></span>TALVERO</div>
  </section>

  <section class="piece letterhead">
    <div class="wordmark"><span class="dot"></span>TALVERO</div>
    <div class="sender">
      <div>Talvero Networks LLC</div>
      <div>PO BOX 418263, Harbor Glen, FL 30999</div>
    </div>
    <div class="contact">
      <div><span class="label">Phone:</span> 954-555-0142</div>
      <div><span class="label">Skype:</span> pennockd</div>
      <div>dwight@talverohub.com</div>
      <div>talverohub.com</div>
    </div>
  </section>

  <section class="piece envelope envelope-black">
    <svg class="flap" width="456" height="120" viewBox="0 0 456 120" aria-hidden="true">
      <polygon points="0,0 456,0 456,14 250,84 206,84 0,14" fill="#262626"/>
    </svg>
    <div class="wordmark light"><span class="dot"></span>TALVERO</div>
  </section>

  <section class="piece envelope envelope-plain">
    <svg class="flap" width="402" height="124" viewBox="0 0 402 124" aria-hidden="true">
      <polyline points="0,0 201,70 402,0" fill="none" stroke="#e3e6ea" stroke-width="1.5"/>
    </svg>
    <div class="wordmark"><span class="dot"></span>TALVERO</div>
  </section>

  <section class="piece envelope envelope-blue">
    <svg class="flap" width="386" height="195" viewBox="0 0 386 195" aria-hidden="true">
      <polygon points="0,0 386,0 386,16 215,76 171,76 0,16" fill="#1aa6e6"/>
    </svg>
    <div class="wordmark"><span class="dot"></span>TALVERO</div>
    <div class="return">
      <div>Talvero Networks LLC</div>
      <div>PO BOX 418263</div>
      <div>Harbor Glen, FL 30999</div>
      <div>dwight@talverohub.com</div>
      <div>talverohub.com</div>
    </div>
  </section>

</body>
</html>
```